Lucien business card

Business card for commercial photography , photographer specialized in advertising, architecture and interior photography, adventure imagery and camera work. 40 years old, worked for the last 20 years. Business card needs to convey a sense of confidence in work achieved. Card needs to be eye catching as will be left behind in many people's offices. Should also mention discreetly NRVB accredited photographer at the verso of the card. Phone number and website link must be apparent easily.

Target Market(s)

Advertising agencies, commercial photography representation

Industry/Entity Type

Architecture

Contact Information for Business Card

Phone number : +61 470 918 264
lucien.marvaux@velmora.example
www.lucienmarvaux.example

Font styles to use
Sans Serif

Requirements
Must have
• Email adress
• Website
• Phone number
• Name
• Photographer
Nice to have
• NRVB accredited photographer
Should not have
• Rond corners

```html
<!DOCTYPE html>
<html lang="en">
<head>
<meta charset="utf-8">
<title>Lucien business card</title>
<link href="https://fonts.googleapis.com/css2?family=Inter:wght@400;700&display=swap" rel="stylesheet">
<style>
  :root {
    --page-bg: #e9e6e2;
    --ink-dark: #1c1a17;
    --ink-light: #ffffff;
    --sky-top: #cdd8e6;
    --sky-low: #e4e7ea;
    --hills: #6f7889;
    --grass-light: #c9a85e;
    --grass-dark: #8a6e35;
    --warm-light: #f1dfbf;
    --warm-mid: #b58e5c;
    --warm-dark: #2a1d12;
    --card-shadow: rgba(0,0,0,0.18);
  }
  * { margin: 0; padding: 0; box-sizing: border-box; }
  html, body {
    width: 1200px; height: 960px; overflow: hidden;
    background: var(--page-bg);
    font-family: "Inter", "Helvetica Neue", Arial, sans-serif;
  }
  .stage {
    width: 1200px; height: 960px;
    display: flex; flex-direction: column; align-items: center; justify-content: center;
    gap: 48px;
  }
  .card {
    position: relative;
    width: 700px; height: 400px;
    border-radius: 0;
    overflow: hidden;
    box-shadow: 0 10px 28px var(--card-shadow);
  }
  .card__photo { position: absolute; inset: 0; }

  /* Verso */
  .card--verso .card__photo {
    background:
      linear-gradient(180deg, transparent 0%, transparent 42%, var(--hills) 48%, var(--grass-light) 56%, var(--grass-dark) 100%),
      linear-gradient(180deg, var(--sky-top) 0%, var(--sky-low) 45%);
  }
  .accreditation {
    position: absolute; top: 30px; right: 36px;
    text-align: right;
    font-size: 30px; font-weight: 400; line-height: 1.15;
    color: var(--ink-dark);
  }

  /* Recto */
  .card--recto .card__photo {
    background: linear-gradient(115deg, var(--warm-light) 0%, var(--warm-mid) 40%, var(--warm-dark) 78%);
  }
  .contact {
    position: absolute; left: 40px; bottom: 34px;
    color: var(--ink-light);
  }
  .contact__name { font-size: 32px; font-weight: 700; line-height: 1.1; }
  .contact__role { font-size: 20px; font-weight: 400; margin-bottom: 14px; }
  .contact__list { list-style: none; }
  .contact__item {
    display: flex; align-items: center; gap: 12px;
    font-size: 19px; line-height: 1.65;
  }
  .contact__icon { width: 18px; height: 18px; flex: none; fill: var(--ink-light); }
</style>
</head>
<body>
<main class="stage">

  <section class="card card--verso">
    <div class="card__photo" role="img" aria-label="Savanna landscape with grazing rhinos, distant blue hills and pale sky"></div>
    <p class="accreditation">NRVB accredited<br>photographer</p>
  </section>

  <section class="card card--recto">
    <div class="card__photo" role="img" aria-label="Backlit silhouette of a photographer aiming a long telephoto lens against warm evening light"></div>
    <div class="contact">
      <h1 class="contact__name">Lucien Marvaux</h1>
      <p class="contact__role">Photographer</p>
      <ul class="contact__list">
        <li class="contact__item">
          <svg class="contact__icon" viewBox="0 0 20 20" aria-hidden="true"><path d="M2 4h16v12H2z M3 5l7 6 7-6" fill="none" stroke="#fff" stroke-width="1.8"/></svg>
          lucien.marvaux@velmora.example
        </li>
        <li class="contact__item">
          <svg class="contact__icon" viewBox="0 0 20 20" aria-hidden="true"><circle cx="10" cy="10" r="8" fill="none" stroke="#fff" stroke-width="1.8"/><path d="M2 10h16M10 2c-4 4-4 12 0 16M10 2c4 4 4 12 0 16" fill="none" stroke="#fff" stroke-width="1.4"/></svg>
          www.lucienmarvaux.example
        </li>
        <li class="contact__item">
          <svg class="contact__icon" viewBox="0 0 20 20" aria-hidden="true"><path d="M6 2h4l1 4-2 2a10 10 0 0 0 3 3l2-2 4 1v4c0 1-1 2-2 2A15 15 0 0 1 4 4c0-1 1-2 2-2z"/></svg>
          +61 470 918 264
        </li>
      </ul>
    </div>
  </section>

</main>
</body>
</html>
```